Quillmoor Tandem Partners needs an email sign off and professional power point template

Newly formed company and we require:1. graphic email signature on our email , and2.a professional powerpoint template (title page and sub pages) and revamp of the attached powerpoint presentation I have uploaded our business car design (logo and contact details ) and a current powerpoint template we are currently working with. Also a brief of how we operateOur mantra is Discover, Develop, Deliver.

Target Market(s)

multinationals and mid size SME's requiring help to grown new markets or geographies for their business.

Colors
000000

Requirements
Must have
• the mantra..our phases of engagement around assisting clients is:
• 1. Discover
• 2. Develop
• 3. Deliver
Nice to have
• we differentiate ourselves form consultant by actually executing the plan for them (i.e. is the delivery phase)

```html
<!DOCTYPE html>
<html lang="en">
<head>
<meta charset="utf-8">
<title>Quillmoor Tandem Partners – Presentation Template</title>
<link href="https://fonts.googleapis.com/css2?family=Bebas+Neue&display=swap" rel="stylesheet">
<style>
  :root {
    --backdrop: #e4e4f6;
    --paper: #ffffff;
    --ink: #000000;
    --brand-blue: #1a6fc0;
    --brand-navy: #1b2a55;
    --muted: #b9b9b9;
    --box-grey: #d9d9d9;
    --box-shadow: #ececec;
    --mark-navy: #1d3a55;
    --mountain-deep: #0d1c2c;
    --mountain-mid: #24506e;
  }
  * { margin: 0; padding: 0; box-sizing: border-box; }
  html, body {
    width: 1037px; height: 1200px; overflow: hidden;
    background: var(--backdrop);
    font-family: "Bebas Neue", "Arial Narrow", sans-serif;
  }
  .stage {
    position: relative; width: 955px; height: 1105px;
    transform: scale(1.08586); transform-origin: 0 0;
  }
  .slide {
    position: absolute; width: 470px; height: 265px;
    background: var(--paper); overflow: hidden;
  }
  .slide svg { display: block; width: 470px; height: 265px; }
  .slide--title { left: 0; top: 0; }
  .slide--banner { left: 485px; top: 0; }
  .slide--venn { left: 0; top: 280px; }
  .slide--quotes-stack { left: 485px; top: 280px; }
  .slide--quotes-row { left: 0; top: 560px; }
  .slide--flow { left: 485px; top: 560px; }
  .slide--cycle { left: 0; top: 840px; }

  text { font-family: "Bebas Neue", "Arial Narrow", sans-serif; }
  .t-ink { fill: var(--ink); }
  .t-white { fill: #fff; }
  .t-blue { fill: var(--brand-blue); }
  .t-navy { fill: var(--brand-navy); }
  .t-muted { fill: var(--muted); }
  .t-mark { fill: var(--mark-navy); }
  .tagline { font-style: italic; }
  .bar { fill: var(--ink); }
  .step-box { fill: var(--box-grey); }
  .step-shadow { fill: var(--box-shadow); }
  .phase-tile { fill: var(--ink); }
  .outline { fill: none; stroke: var(--ink); stroke-width: 3; }
  .photo-deep { fill: url(#photoTone); }
</style>
</head>
<body>
<div class="stage">

  <!-- Title slide -->
  <section class="slide slide--title">
    <svg viewBox="0 0 470 265">
      <defs>
        <linearGradient id="mountainTone" x1="0" y1="0" x2="0" y2="1">
          <stop offset="0" stop-color="var(--mountain-mid)"/>
          <stop offset="1" stop-color="var(--mountain-deep)"/>
        </linearGradient>
      </defs>
      <rect x="0" y="0" width="187" height="265" fill="url(#mountainTone)" role="img" aria-label="Misty blue mountain range backdrop"/>
      <text class="t-white" x="93" y="126" font-size="34" text-anchor="middle">HALLWICK</text>
      <text class="t-white" x="93" y="150" font-size="16" text-anchor="middle" letter-spacing="1">BUSINESS DEVELOPERS</text>

      <text class="t-ink" x="320" y="92" font-size="38" text-anchor="middle">QUILLMOOR</text>
      <text class="t-ink" x="320" y="139" font-size="38" text-anchor="middle">TANDEM</text>
      <text class="t-ink" x="320" y="186" font-size="38" text-anchor="middle">PARTNERS</text>
      <text class="t-ink tagline" x="320" y="216" font-size="19" text-anchor="middle">DISCOVER, DEVELOP, DELIVER</text>
      <text class="t-muted" x="320" y="248" font-size="20" text-anchor="middle">12<tspan font-size="12" dy="-7">TH</tspan><tspan dy="7"> DECEMBER 2018</tspan></text>
    </svg>
  </section>

  <!-- Banner title slide -->
  <section class="slide slide--banner">
    <svg viewBox="0 0 470 265">
      <rect class="bar" x="0" y="0" width="470" height="143"/>
      <rect class="bar" x="0" y="148" width="470" height="5"/>
      <text class="t-white" x="235" y="72" font-size="30" text-anchor="middle">HALLWICK</text>
      <text class="t-white" x="235" y="94" font-size="14" text-anchor="middle" letter-spacing="1">BUSINESS DEVELOPERS</text>
      <text class="t-blue" x="235" y="200" font-size="36" text-anchor="middle">QUILLMOOR TANDEM PARTNERS</text>
      <text class="t-navy tagline" x="235" y="231" font-size="19" text-anchor="middle">DISCOVER, DEVELOP, DELIVER</text>
      <text class="t-muted" x="235" y="258" font-size="17" text-anchor="middle">12<tspan font-size="10" dy="-6">TH</tspan><tspan dy="6"> DECEMBER 2018</tspan></text>
    </svg>
  </section>

  <!-- Venn process slide -->
  <section class="slide slide--venn">
    <svg viewBox="0 0 470 265">
      <rect class="bar" x="0" y="0" width="70" height="11"/>
      <rect class="bar" x="75" y="0" width="395" height="11"/>
      <rect class="bar" x="0" y="255" width="395" height="10"/>
      <rect class="bar" x="400" y="255" width="70" height="10"/>
      <text class="t-ink" x="5" y="38" font-size="22">ALIGNING</text>
      <text class="t-ink" x="5" y="66" font-size="22">OUR PROCESS</text>
      <line x1="0" y1="72" x2="110" y2="72" stroke="var(--ink)" stroke-width="1.5"/>
      <circle cx="110" cy="72" r="3.5" fill="var(--ink)"/>
      <circle class="outline" cx="300" cy="81" r="69"/>
      <circle class="outline" cx="251" cy="173" r="69"/>
      <circle class="outline" cx="350" cy="173" r="69"/>
      <text class="t-ink" x="299" y="71" font-size="15" text-anchor="middle">DEVELOP</text>
      <text class="t-ink" x="300" y="155" font-size="15" text-anchor="middle">YOU</text>
      <text class="t-ink" x="228" y="179" font-size="15" text-anchor="middle">DISCOVER</text>
      <text class="t-ink" x="376" y="179" font-size="15" text-anchor="middle">DELIVER</text>
      <rect x="420" y="222" width="30" height="40" fill="#fff"/>
      <text class="t-mark" x="435" y="246" font-size="9" text-anchor="middle">HALLWICK</text>
    </svg>
  </section>

  <!-- Testimonials, stacked -->
  <section class="slide slide--quotes-stack">
    <svg viewBox="0 0 470 265">
      <defs>
        <linearGradient id="photoTone" x1="0" y1="0" x2="1" y2="1">
          <stop offset="0" stop-color="#8a8a84"/>
          <stop offset="1" stop-color="#3e3a36"/>
        </linearGradient>
      </defs>
      <rect class="bar" x="0" y="0" width="70" height="11"/>
      <rect class="bar" x="75" y="0" width="395" height="11"/>
      <rect class="bar" x="0" y="255" width="395" height="10"/>
      <rect class="bar" x="400" y="255" width="70" height="10"/>
      <circle class="photo-deep" cx="70" cy="62" r="40" role="img" aria-label="Portrait photo of a client working on a laptop"/>
      <circle class="photo-deep" cx="411" cy="136" r="40" role="img" aria-label="Portrait photo of a client at a laptop outdoors"/>
      <circle class="photo-deep" cx="71" cy="205" r="40" role="img" aria-label="Portrait photo of a client seated with a laptop"/>
      <text class="t-ink" x="132" y="60" font-size="34">“</text>
      <text class="t-ink" x="430" y="97" font-size="34">”</text>
      <text class="t-ink" x="37" y="142" font-size="34">“</text>
      <text class="t-ink" x="336" y="178" font-size="34">”</text>
      <text class="t-ink" x="116" y="208" font-size="34">“</text>
      <text class="t-ink" x="400" y="245" font-size="34">”</text>
      <rect x="420" y="222" width="30" height="40" fill="#fff"/>
      <text class="t-mark" x="435" y="246" font-size="9" text-anchor="middle">HALLWICK</text>
    </svg>
  </section>

  <!-- Testimonials, row -->
  <section class="slide slide--quotes-row">
    <svg viewBox="0 0 470 265">
      <rect class="bar" x="0" y="0" width="70" height="11"/>
      <rect class="bar" x="75" y="0" width="395" height="11"/>
      <rect class="bar" x="0" y="255" width="395" height="10"/>
      <rect class="bar" x="400" y="255" width="70" height="10"/>
      <circle class="photo-deep" cx="73" cy="67" r="40" role="img" aria-label="Portrait photo of a client working on a laptop"/>
      <circle class="photo-deep" cx="235" cy="67" r="40" role="img" aria-label="Portrait photo of a client at a laptop outdoors"/>
      <circle class="photo-deep" cx="398" cy="67" r="40" role="img" aria-label="Portrait photo of a client seated with a laptop"/>
      <text class="t-ink" x="80" y="152" font-size="34" text-anchor="middle">“</text>
      <text class="t-ink" x="235" y="152" font-size="34" text-anchor="middle">“</text>
      <text class="t-ink" x="400" y="152" font-size="34" text-anchor="middle">“</text>
      <text class="t-ink" x="80" y="250" font-size="34" text-anchor="middle">”</text>
      <text class="t-ink" x="235" y="250" font-size="34" text-anchor="middle">”</text>
      <text class="t-ink" x="400" y="250" font-size="34" text-anchor="middle">”</text>
      <rect x="420" y="222" width="30" height="40" fill="#fff"/>
      <text class="t-mark" x="435" y="246" font-size="9" text-anchor="middle">HALLWICK</text>
    </svg>
  </section>

  <!-- Opportunity planning flow -->
  <section class="slide slide--flow">
    <svg viewBox="0 0 470 265">
      <rect class="bar" x="5" y="7" width="4" height="68"/>
      <text class="t-ink" x="13" y="24" font-size="19">OPPORTUNITY</text>
      <text class="t-ink" x="13" y="48" font-size="19">PLANNING</text>
      <text class="t-ink" x="13" y="74" font-size="19">PROCESS</text>

      <g class="step">
        <rect class="step-shadow" x="104" y="17" width="62" height="57"/>
        <rect class="step-box" x="100" y="13" width="62" height="57"/>
        <text class="t-ink" x="131" y="37" font-size="13" text-anchor="middle">IDENTIFY</text>
        <text class="t-ink" x="131" y="53" font-size="13" text-anchor="middle">OPPORTUNITY</text>
      </g>
      <polygon class="bar" points="167,37 192,37 192,31 205,41 192,51 192,45 167,45"/>
      <g class="step">
        <rect class="step-shadow" x="211" y="17" width="72" height="57"/>
        <rect class="step-box" x="207" y="13" width="72" height="57"/>
        <text class="t-ink" x="243" y="28" font-size="13" text-anchor="middle">QUALIFY</text>
        <text class="t-ink" x="243" y="44" font-size="13" text-anchor="middle">OPPORTUNITY</text>
        <text class="t-ink" x="243" y="60" font-size="13" text-anchor="middle">(DISCOVER)</text>
      </g>
      <polygon class="bar" points="283,37 302,37 302,31 315,41 302,51 302,45 283,45"/>
      <g class="step">
        <rect class="step-shadow" x="319" y="17" width="141" height="57"/>
        <rect class="step-box" x="315" y="13" width="141" height="57"/>
        <text class="t-ink" x="385" y="28" font-size="13" text-anchor="middle">IDENTIFY KEY INDIVIDUALS OF</text>
        <text class="t-ink" x="385" y="44" font-size="13" text-anchor="middle">INFLUENCE TO DECISION</text>
        <text class="t-ink" x="385" y="60" font-size="13" text-anchor="middle">PROCESS</text>
      </g>
      <polygon class="bar" points="371,80 379,80 379,88 385,88 375,98 365,88 371,88"/>
      <g class="step">
        <rect class="step-shadow" x="319" y="107" width="141" height="57"/>
        <rect class="step-box" x="315" y="103" width="141" height="57"/>
        <text class="t-ink" x="385" y="119" font-size="13" text-anchor="middle">DEVELOP</text>
        <text class="t-ink" x="385" y="135" font-size="13" text-anchor="middle">&amp; IMPLEMENT SALES</text>
        <text class="t-ink" x="385" y="151" font-size="13" text-anchor="middle">STRATEGY &amp; PLAN</text>
      </g>
      <polygon class="bar" points="371,168 379,168 379,178 385,178 375,190 365,178 371,178"/>
      <g class="step">
        <rect class="step-shadow" x="319" y="199" width="141" height="57"/>
        <rect class="step-box" x="315" y="195" width="141" height="57"/>
        <text class="t-ink" x="385" y="211" font-size="13" text-anchor="middle">ALIGN &amp; DEVELOP</text>
        <text class="t-ink" x="385" y="227" font-size="13" text-anchor="middle">RELATIONSHIPS WITH</text>
        <text class="t-ink" x="385" y="243" font-size="13" text-anchor="middle">KEY PEOPLE OF INFLUENCE</text>
      </g>
      <polygon class="bar" points="312,222 293,222 293,216 280,226 293,236 293,230 312,230"/>
      <g class="step">
        <rect class="step-shadow" x="174" y="199" width="105" height="57"/>
        <rect class="step-box" x="170" y="195" width="105" height="57"/>
        <text class="t-ink" x="222" y="211" font-size="13" text-anchor="middle">EXECUTE PLAN</text>
        <text class="t-ink" x="222" y="227" font-size="13" text-anchor="middle">AND DELIVER</text>
        <text class="t-ink" x="222" y="243" font-size="13" text-anchor="middle">PROPOSAL</text>
      </g>
      <polygon class="bar" points="163,222 138,222 138,216 125,226 138,236 138,230 163,230"/>
      <g class="step">
        <rect class="step-shadow" x="19" y="199" width="102" height="57"/>
        <rect class="step-box" x="15" y="195" width="102" height="57"/>
        <text class="t-ink" x="66" y="219" font-size="13" text-anchor="middle">NEGOTIATE</text>
        <text class="t-ink" x="66" y="235" font-size="13" text-anchor="middle">AND SIGN</text>
      </g>

      <rect class="phase-tile" x="15" y="85" width="94" height="97"/>
      <rect class="phase-tile" x="115" y="85" width="93" height="97"/>
      <rect class="phase-tile" x="214" y="85" width="93" height="97"/>
      <text class="t-white" x="62" y="140" font-size="20" text-anchor="middle">DISCOVER</text>
      <text class="t-white" x="161" y="140" font-size="20" text-anchor="middle">DEVELOP</text>
      <text class="t-white" x="260" y="140" font-size="20" text-anchor="middle">DELIVER</text>
    </svg>
  </section>

  <!-- Opportunity planning cycle -->
  <section class="slide slide--cycle">
    <svg viewBox="0 0 470 265">
      <rect class="bar" x="0" y="0" width="70" height="11"/>
      <rect class="bar" x="75" y="0" width="395" height="11"/>
      <rect class="bar" x="0" y="255" width="395" height="10"/>
      <rect class="bar" x="400" y="255" width="70" height="10"/>
      <text class="t-ink" x="5" y="38" font-size="22">OPPORTUNITY</text>
      <text class="t-ink" x="5" y="66" font-size="22">PLANNING PROCESS</text>
      <line x1="0" y1="73" x2="150" y2="73" stroke="var(--ink)" stroke-width="1.5"/>
      <circle cx="150" cy="73" r="3.5" fill="var(--ink)"/>

      <circle cx="290" cy="142" r="100" fill="none" stroke="var(--ink)" stroke-width="11"/>
      <polygon class="bar" points="236,36 254,45 237,58"/>

      <text class="t-ink" x="290" y="102" font-size="24" text-anchor="middle">DISCOVER</text>
      <text class="t-ink" x="290" y="133" font-size="24" text-anchor="middle">DEVELOP</text>
      <text class="t-ink" x="290" y="164" font-size="24" text-anchor="middle">DELIVER</text>

      <g font-size="9">
        <rect class="step-box" x="255" y="20" width="68" height="45" rx="6"/>
        <text class="t-ink" x="289" y="38" text-anchor="middle">IDENTIFY</text>
        <text class="t-ink" x="289" y="51" text-anchor="middle">OPPORTUNITY</text>

        <rect class="step-box" x="343" y="50" width="64" height="48" rx="6"/>
        <text class="t-ink" x="375" y="66" text-anchor="middle">QUALIFY</text>
        <text class="t-ink" x="375" y="78" text-anchor="middle">OPPORTUNITY</text>
        <text class="t-ink" x="375" y="90" text-anchor="middle">(DISCOVER)</text>

        <rect class="step-box" x="345" y="110" width="80" height="62" rx="6"/>
        <text class="t-ink" x="385" y="126" text-anchor="middle">IDENTIFY</text>
        <text class="t-ink" x="385" y="138" text-anchor="middle">KEY INDIVIDUALS OF</text>
        <text class="t-ink" x="385" y="150" text-anchor="middle">INFLUENCE TO</text>
        <text class="t-ink" x="385" y="162" text-anchor="middle">DECISION PROCESS</text>

        <rect class="step-box" x="288" y="180" width="66" height="67" rx="6"/>
        <text class="t-ink" x="321" y="196" text-anchor="middle">DEVELOP</text>
        <text class="t-ink" x="321" y="208" text-anchor="middle">&amp; IMPLEMENT</text>
        <text class="t-ink" x="321" y="220" text-anchor="middle">SALES</text>
        <text class="t-ink" x="321" y="232" text-anchor="middle">STRATEGY &amp; PLAN</text>

        <rect class="step-box" x="200" y="175" width="68" height="72" rx="6"/>
        <text class="t-ink" x="234" y="187" text-anchor="middle">ALIGN &amp; DEVELOP</text>
        <text class="t-ink" x="234" y="199" text-anchor="middle">RELATIONSHIPS</text>
        <text class="t-ink" x="234" y="211" text-anchor="middle">WITH</text>
        <text class="t-ink" x="234" y="227" text-anchor="middle">KEY PEOPLE OF</text>
        <text class="t-ink" x="234" y="241" text-anchor="middle">INFLUENCE</text>

        <rect class="step-box" x="158" y="113" width="68" height="50" rx="6"/>
        <text class="t-ink" x="192" y="128" text-anchor="middle">EXECUTE PLAN</text>
        <text class="t-ink" x="192" y="141" text-anchor="middle">AND DELIVER</text>
        <text class="t-ink" x="192" y="154" text-anchor="middle">PROPOSAL</text>

        <rect class="step-box" x="173" y="57" width="68" height="43" rx="6"/>
        <text class="t-ink" x="207" y="74" text-anchor="middle">NEGOTIATE</text>
        <text class="t-ink" x="207" y="87" text-anchor="middle">AND SIGN</text>
      </g>

      <rect x="420" y="222" width="30" height="40" fill="#fff"/>
      <text class="t-mark" x="435" y="246" font-size="9" text-anchor="middle">HALLWICK</text>
    </svg>
  </section>

</div>
</body>
</html>
```